We would like to incorporate our logo into letterhead design and envelopes. We are looking for something that is moderately conservative but not old law firm style. Both the envelopes and the letterhead must have both firm addresses. We would like to incorporate the color of the logo, but only a small amount of color - perhaps on one of the borders. The addresses for the firm locations are listed below. Given that it is a law firm, it needs to somewhat conservative, but not the old school, small black font on cream colored paper design.

The firm addresses are:

27815 N. Harlow Pemberton Pkwy.
Ste 4200
Scottsdale, AZ 85391

6100 W. Cedar Avenue
Ste 700
Burbank, CA 91623

Industry/Entity Type

Legal

Colors

Designer to choose colors to be used in the design.

Requirements
Must have
• Both addresses:
• 27815 N. Harlow Pemberton Pkwy.
• Ste 4200
• Scottsdale, AZ 85391
• 6100 W. Cedar Avenue
• Ste 700
• Burbank, CA 91623
Nice to have
• Small amount of color on border(s) that matches the logo but not too much color

```html
<!DOCTYPE html>
<html lang="en">
<head>
<meta charset="utf-8">
<title>Marlow Pike Law – Stationery</title>
<link href="https://fonts.googleapis.com/css2?family=Marcellus&family=Poppins:wght@400&display=swap" rel="stylesheet">
<style>
  :root {
    --backdrop: #e4e4e5;
    --paper: #efe8d6;
    --navy: #241f5e;
    --ink: #1c1a22;
    --cream-text: #efe8d6;
  }
  * { margin: 0; padding: 0; box-sizing: border-box; }
  html, body { width: 1200px; height: 882px; overflow: hidden; }
  body {
    background: var(--backdrop);
    position: relative;
    font-family: "Poppins", sans-serif;
  }
  .firm-name {
    font-family: "Marcellus", serif;
    color: var(--navy);
    letter-spacing: 0.01em;
    white-space: nowrap;
    line-height: 1;
  }
  .envelope {
    position: absolute;
    left: 106px;
    width: 473px;
    background: var(--paper);
  }
  .envelope-front { top: 310px; height: 215px; }
  .envelope-front .firm-name {
    position: absolute; left: 32px; top: 31px; font-size: 24px;
  }
  .return-address {
    position: absolute; left: 32px; font-size: 7.6px; line-height: 9.6px; color: var(--ink);
  }
  .return-address.az { top: 66px; }
  .return-address.ca { top: 100px; }
  .envelope-back { top: 565px; height: 217px; }
  .flap { position: absolute; left: 0; top: 0; width: 473px; height: 79px; }
  .flap svg { display: block; }
  .flap .firm-name {
    position: absolute; left: 0; right: 0; top: 30px; text-align: center;
    font-size: 17px; color: var(--cream-text);
  }
  .letterhead {
    position: absolute; left: 605px; top: 78px; width: 497px; height: 704px;
    background: var(--paper);
  }
  .letterhead .firm-name {
    position: absolute; left: 0; right: 0; top: 50px; text-align: center; font-size: 30px;
  }
  .letterhead-footer {
    position: absolute; left: 0; right: 0; top: 650px; height: 29px;
    background: var(--navy); color: #fff;
    font-size: 7.6px; line-height: 12px; text-align: center; padding-top: 2px;
  }
</style>
</head>
<body>
  <section class="envelope envelope-front">
    <div class="firm-name">MARLOW PIKE LAW</div>
    <address class="return-address az" style="font-style:normal">
      27815 N. Harlow Pemberton Pkwy.<br>Ste 4200<br>Scottsdale, AZ 85391
    </address>
    <address class="return-address ca" style="font-style:normal">
      6100 W. Cedar Avenue<br>Ste 700<br>Burbank, CA 91623
    </address>
  </section>

  <section class="envelope envelope-back">
    <div class="flap">
      <svg width="473" height="79" viewBox="0 0 473 79">
        <path d="M0 0 H473 L462 50 Q456 79 428 79 H45 Q17 79 11 50 Z" fill="var(--navy)"/>
      </svg>
      <div class="firm-name">MARLOW PIKE LAW</div>
    </div>
  </section>

  <section class="letterhead">
    <div class="firm-name">MARLOW PIKE LAW</div>
    <footer class="letterhead-footer">
      6100 W. Cedar Avenue, Ste 700, Burbank, CA 91623<br>
      27815 N. Harlow Pemberton Pkwy., Ste 4200, Scottsdale, AZ 85391
    </footer>
  </section>
</body>
</html>
```